Web Page Template and Logo Design

We are launching a website to sell homewares and would like a logo design, as well as a home page template, and the template for the product pages.

The homewares store is called Saucy Newt. The homewares we will sell will be edgy and very bright colours. We envisage the theme of the homepage will have hot pink, some blue/ white chinioserie pattern and potentially lime green. We would like the logo to reflect humour and "Saucy Newt".

The images uploaded reflect the look and feel of the type of people who are our customers - they are not minimalists and they are definitely not into beige!

Target Market(s)

Predominantly women, 30 - 50

Industry/Entity Type

Store

Number of Pages Required

2 page

Font styles to use
Sans Serif

Colors
e34197
acd036
33a6d7

Requirements
Must have
• Template for home page and standard template for other pages;PLEASE NOTE: I have now listed the Saucy Newt Logo as a separate 2 day listing; a bright, bold, colourful website with a sense of humour (it needs to dare people to put something bright in their homes).
• Please Note: I don't need a whole website, I have one of my staff who can do that for me. I just want the creative template for the homepage and a standard template for the product pages. It is the graphic design and creative side I am more interested in. I will want my staff member to be able to take the design and incorporate it into the website.

```html
<!DOCTYPE html>
<html lang="en">
<head>
<meta charset="utf-8">
<title>Saucy Newt</title>
<link href="https://fonts.googleapis.com/css2?family=Mulish:wght@300;400;600&family=Lustria&display=swap" rel="stylesheet">
<style>
:root{
  --lime:#acd036;
  --lime-dark:#8fba1f;
  --pink:#e34197;
  --pink-soft:#ff7fc6;
  --blue:#33a6d7;
  --sky:#5bc8f5;
  --ink:#333;
  --grey:#777;
  --footer:#f4f4f4;
  --line:#ddd;
}
*{box-sizing:border-box;margin:0;padding:0}
html,body{width:1108px;height:1200px;overflow:hidden;background:#fff}
body{position:relative;font-family:'Mulish',sans-serif;color:var(--ink)}
.abs{position:absolute}

.site-header{left:0;top:0;width:1108px;height:103px;background:linear-gradient(#bfdc3f,var(--lime-dark))}
.brand{left:116px;top:22px;color:#fff}
.brand-name{font-size:34px;font-weight:400;line-height:1;letter-spacing:-0.5px}
.brand-slogan{font-size:13px;font-weight:300;margin-top:8px;margin-left:4px}
.main-nav{top:44px;left:503px;display:flex;gap:0}
.main-nav a{position:absolute;color:#fff;text-decoration:none;font-size:16px;white-space:nowrap}

.hero{left:0;top:103px;width:1108px;height:447px;background:#fff;border-bottom:1px solid #eee}
.hero-art{left:0;top:0}
.hero-kicker{left:117px;top:120px;font-family:'Lustria',serif;font-size:29px;color:var(--pink)}
.hero-title{left:117px;top:155px;font-family:'Lustria',serif;font-size:35px;color:var(--blue)}
.hero-text{left:118px;top:197px;font-size:11.5px;line-height:19px;color:var(--grey);width:330px}
.btn{display:flex;align-items:center;justify-content:center;background:linear-gradient(#b7d93b,var(--lime-dark));color:#fff;font-size:12px;font-weight:600;border-radius:2px;text-transform:uppercase}
.hero-btn{left:117px;top:244px;width:104px;height:30px}
.slider-dots{left:117px;top:289px;display:flex;gap:4px}
.slider-dots span{width:12px;height:12px;border-radius:50%;background:#d6d6d6}
.slider-dots span.active{background:var(--pink)}

.category{top:575px;width:211px;height:250px}
.category svg.shape{position:absolute;left:0;top:0}
.category-photo{position:absolute;left:10px;top:12px;width:191px;height:113px}
.category-title{position:absolute;left:16px;top:133px;font-family:'Lustria',serif;font-size:21px;color:#fff}
.category-text{position:absolute;left:16px;top:162px;width:190px;font-size:11px;line-height:17px;color:#fff}
.category-link{position:absolute;left:16px;top:201px;font-size:11.5px;color:#444}

.welcome-title{left:122px;top:866px;font-size:26px;font-weight:300;color:#333}
.welcome-text{left:127px;top:908px;width:610px;font-size:11.5px;line-height:19px;color:var(--grey)}
.welcome-text p+p{margin-top:13px}

.gallery-photo{left:766px;top:858px;width:225px;height:103px;border:1px solid #e6e6e6}
.gallery-title{left:767px;top:965px;font-size:17px;color:var(--pink);font-weight:300}
.gallery-text{left:770px;top:991px;font-size:10.5px;color:var(--grey)}
.gallery-btn{left:770px;top:1010px;width:92px;height:27px;font-size:11px}

.site-footer{left:0;top:1095px;width:1108px;height:105px;background:linear-gradient(#fff,var(--footer));border-top:1px solid var(--line)}
.footer-nav{left:118px;top:1121px;font-size:15px;color:#333;white-space:nowrap}
.footer-nav span{margin:0 6px;color:#555}
.copyright{left:118px;top:1150px;font-size:11.5px;color:#555}
.social{left:875px;top:1123px;display:flex;gap:9px}
.social span{width:22px;height:22px;border-radius:2px}
</style>
</head>
<body>

<header class="abs site-header">
  <div class="abs brand">
    <div class="brand-name">Saucy Newt</div>
    <div class="brand-slogan">Slogan goes here</div>
  </div>
  <nav class="abs main-nav">
    <a style="left:0">Home</a>
    <a style="left:82px">About Us</a>
    <a style="left:186px">Contact Us</a>
    <a style="left:305px">Products</a>
    <a style="left:407px">Gallery</a>
  </nav>
</header>

<section class="abs hero">
  <svg class="abs hero-art" width="1108" height="447" role="img" aria-label="Photo of a blue and white chinoiserie vase of pink roses against a hot pink lattice wallpaper">
    <defs>
      <linearGradient id="heroFill" x1="0" y1="0" x2="1" y2="1">
        <stop offset="0" stop-color="#f3a6cc"/>
        <stop offset="0.45" stop-color="#f7d3e4"/>
        <stop offset="0.7" stop-color="#6d86c8"/>
        <stop offset="1" stop-color="#e9eef4"/>
      </linearGradient>
    </defs>
    <path d="M565,0 C520,100 555,220 520,320 C500,375 462,415 428,447 H1108 V0 Z" fill="url(#heroFill)"/>
  </svg>
  <div class="abs hero-kicker">Curabitur iaculis tempus</div>
  <div class="abs hero-title">Morbinare gravida elit</div>
  <p class="abs hero-text">Morbi diam mauris viverra in gravida eu mattis in ante Morbi eget arcu Morbi porta libero id ullamcorper nonum</p>
  <div class="abs btn hero-btn">Read More</div>
  <div class="abs slider-dots"><span class="active"></span><span></span><span></span><span></span></div>
</section>

<article class="abs category" style="left:120px">
  <svg class="shape" width="211" height="250"><defs><linearGradient id="gBlue" x1="0" y1="0" x2="1" y2="0"><stop offset="0" stop-color="#3da3e0"/><stop offset="1" stop-color="#6fd0f8"/></linearGradient></defs><ellipse cx="110" cy="237" rx="95" ry="5" fill="#000" opacity=".08"/><path d="M0,0 H211 V231 Q160,222 110,230 Q55,238 0,230 Z" fill="url(#gBlue)"/></svg>
  <div class="category-photo" role="img" aria-label="Photo of a bright room with a zebra figure and lamps" style="background:linear-gradient(135deg,#f4f1ea,#9a8f86 60%,#e8e4dc)"></div>
  <h3 class="category-title">Lights</h3>
  <p class="category-text">Morbi diam mauris viverra in gr avida eu mattis in ante eget nibh ligula</p>
  <a class="category-link">Read More</a>
</article>

<article class="abs category" style="left:340px">
  <svg class="shape" width="211" height="250"><defs><linearGradient id="gPink" x1="0" y1="0" x2="1" y2="0"><stop offset="0" stop-color="#f766b8"/><stop offset="1" stop-color="#ff8fd0"/></linearGradient></defs><ellipse cx="110" cy="237" rx="95" ry="5" fill="#000" opacity=".08"/><path d="M0,0 H211 V231 Q160,222 110,230 Q55,238 0,230 Z" fill="url(#gPink)"/></svg>
  <div class="category-photo" role="img" aria-label="Photo of blue and white porcelain on patterned tiles" style="background:linear-gradient(135deg,#e7eef8,#3158b0 55%,#c9d6ee)"></div>
  <h3 class="category-title">Homewares</h3>
  <p class="category-text">Morbi diam mauris viverra in gr avida eu mattis in ante eget nibh ligula</p>
  <a class="category-link">Read More</a>
</article>

<article class="abs category" style="left:561px">
  <svg class="shape" width="211" height="250"><defs><linearGradient id="gLime" x1="0" y1="0" x2="1" y2="0"><stop offset="0" stop-color="#a8cc2c"/><stop offset="1" stop-color="#c2de3e"/></linearGradient></defs><ellipse cx="110" cy="237" rx="95" ry="5" fill="#000" opacity=".08"/><path d="M0,0 H211 V231 Q160,222 110,230 Q55,238 0,230 Z" fill="url(#gLime)"/></svg>
  <div class="category-photo" role="img" aria-label="Photo of a floral armchair against pink wallpaper" style="background:linear-gradient(135deg,#e77aa7,#f2c9d8 50%,#c83c5c)"></div>
  <h3 class="category-title">Furniture</h3>
  <p class="category-text">Morbi diam mauris viverra in gr avida eu mattis in ante eget nibh ligula</p>
  <a class="category-link">Read More</a>
</article>

<article class="abs category" style="left:781px">
  <svg class="shape" width="211" height="250"><defs><linearGradient id="gSky" x1="0" y1="0" x2="1" y2="0"><stop offset="0" stop-color="#43b8ee"/><stop offset="1" stop-color="#62cdf7"/></linearGradient></defs><ellipse cx="110" cy="237" rx="95" ry="5" fill="#000" opacity=".08"/><path d="M0,0 H211 V231 Q160,222 110,230 Q55,238 0,230 Z" fill="url(#gSky)"/></svg>
  <div class="category-photo" role="img" aria-label="Colourful painted artwork on white" style="background:linear-gradient(90deg,#fff,#e25a55 45%,#6c8fc0 75%,#fff)"></div>
  <h3 class="category-title">Art Work</h3>
  <p class="category-text">Morbi diam mauris viverra in gr avida eu mattis in ante eget nibh ligula</p>
  <a class="category-link">Read More</a>
</article>

<h1 class="abs welcome-title">Welcome to Our Website Mainpage</h1>
<div class="abs welcome-text">
  <p>Vivamus porttitor purus nisi eleifend libero a tempus libero lectus feugiat felis Morbi diam mauris viverra in gravida eu mattis in ante Morbi eget arcu Morbi porta libero id ullamcorper nonummy nibh</p>
  <p>Curabitur iaculis tempus eros Curabitur vel mi sit amet magna malesuada ultrices Ut nisi erat fermentum vel congue id euismod in elit Fusce ultricies orci ac feugiat suscipit leo massa sodales velit etVivamus porttitor purus nisi eleif-end libero a tempus libero lectus feugiat felis Morbi diam mauris viverra in gravida eu mattis in ante Morbi eget arcu Morbi porta libero id ullamcorper nonummy nibh ligula</p>
</div>

<div class="abs gallery-photo" role="img" aria-label="Photo of a yellow wicker chair with a pink cushion" style="background:linear-gradient(90deg,#f3eef2,#e8436a 40%,#f3d22a 70%,#d8c23a)"></div>
<div class="abs gallery-title">View Our Gallery</div>
<div class="abs gallery-text">Eleifend libero a tempus libero lectus feugiat</div>
<div class="abs btn gallery-btn">View More</div>

<footer class="abs site-footer"></footer>
<nav class="abs footer-nav">Home<span>|</span>About Us<span>|</span>Contact Us<span>|</span>Products<span>|</span>Gallery</nav>
<div class="abs copyright">© 2014 Company Name&nbsp; All right reserved&nbsp; Term of Use</div>
<div class="abs social">
  <span style="background:#3b5b9a"></span>
  <span style="background:#3fb5e6"></span>
  <span style="background:#1b74b0"></span>
  <span style="background:#f08a1c"></span>
</div>

</body>
</html>
```